Solvane Travel Planners needs an bold logo and business card design

Thanks you all for helping me with this project your assistance is appriciated
I am starting a home based travel agency and I need a bold and eye catching logo and business card designed.
I want to convey a sense of FREEDOM, expertise, customer service for travel customers
Solvane travel planners is a full service travel agency focused on customer service and adding value to a vacation and travel planning.
my idea is for a card that looks like an cruise ship boarding pass or passport with stamps with a back drop of beautiful beach scene, resort hotel and happiness.
The logo should be eye catching, unique but give a sense of freedom and it should be travel related
We want to give customers a sense of Freedom from travel planning, freedom from researching cruises and hotels and freedom to enjoy a wonderful cost effective vacation.

Target Market(s)

Customers considering travel for vacations, family reunions, business and weddings

Industry/Entity Type

Travel Industry

Contact Information for Business Card

Solvane Travel Planners
Marcus Helbrook Owner
MHelbrook@SolvaneTravelPlanners.com
SolvaneTravelPlanners.com
(555) 214-7830

Logo Text

“One’s destination is never a place, but a new way of seeing things.”

Font styles to use
Serif

Colors
85cae6
0492cd
ec1f27
e667a6
b768aa
33b8a4

Requirements
Must have
• The Logo you create should be on the busoness card
• should be clean, easy to read and attractive
• something you that would make you want to work with a travel agent
Nice to have
• should have cruise ship, hotel on the card or something that conveys travel
Should not have
• Should not have the american flag
• no yellow on the card

```html
<!DOCTYPE html>
<html lang="en">
<head>
<meta charset="utf-8">
<title>Solvane Travel Planners — Business Card</title>
<link rel="stylesheet" href="https://fonts.googleapis.com/css2?family=Open+Sans:wght@400;600&display=swap">
<style>
  :root {
    --backdrop: #e9e7e6;
    --card: #fbfafa;
    --violet: #b768aa;
    --ink: #3a3a3a;
    --icon: #a0568f;
  }
  html, body {
    margin: 0;
    width: 1200px;
    height: 900px;
    overflow: hidden;
    background: var(--backdrop);
    font-family: "Open Sans", Arial, sans-serif;
  }
  .card {
    position: absolute;
    left: 240px;
    top: 210px;
    width: 720px;
    height: 444px;
    background: var(--card);
    box-shadow: 0 10px 30px rgba(0,0,0,0.12);
    overflow: hidden;
  }
  .identity {
    position: absolute;
    left: 46px;
    top: 34px;
  }
  .identity__name {
    margin: 0;
    font-size: 26px;
    font-weight: 600;
    color: var(--violet);
    line-height: 1.2;
  }
  .identity__role {
    margin: 2px 0 0;
    font-size: 22px;
    color: var(--ink);
  }
  .contacts {
    list-style: none;
    margin: 0;
    padding: 0;
    position: absolute;
    left: 46px;
    top: 112px;
  }
  .contacts__item {
    display: flex;
    align-items: center;
    gap: 10px;
    font-size: 19.5px;
    color: var(--ink);
    line-height: 25px;
  }
  .contacts__icon {
    width: 14px;
    height: 14px;
    fill: var(--icon);
    flex: none;
  }
  .brand {
    position: absolute;
    right: 34px;
    top: 290px;
    display: flex;
    align-items: center;
    gap: 12px;
  }
  .brand__dot {
    width: 26px;
    height: 26px;
    border-radius: 50%;
    background: var(--violet);
  }
  .brand__name {
    font-size: 30px;
    font-weight: 600;
    color: var(--violet);
    white-space: nowrap;
  }
  .footer-band {
    position: absolute;
    left: 0;
    bottom: 0;
    width: 100%;
    height: 62px;
    background: var(--violet);
  }
</style>
</head>
<body>
  <article class="card">
    <header class="identity">
      <h1 class="identity__name">Marcus Helbrook</h1>
      <p class="identity__role">Owner</p>
    </header>
    <ul class="contacts">
      <li class="contacts__item">
        <svg class="contacts__icon" viewBox="0 0 16 16" aria-hidden="true"><path d="M1 5c0-2 3-3 7-3s7 1 7 3v1h-3V5H4v1H1zM3 7h10l1 7H2zM8 9a2 2 0 1 0 0 4 2 2 0 0 0 0-4z"/></svg>
        (555) 214-7830
      </li>
      <li class="contacts__item">
        <svg class="contacts__icon" viewBox="0 0 16 16" aria-hidden="true"><path d="M1 3h14v10H1zM2 4l6 5 6-5v1L8 10 2 5z" fill-rule="evenodd"/></svg>
        MHelbrook@SolvaneTravelPlanners.com
      </li>
      <li class="contacts__item">
        <svg class="contacts__icon" viewBox="0 0 16 16" aria-hidden="true"><path d="M6 10l4-4M7 4l2-2a3 3 0 0 1 5 5l-2 2M9 12l-2 2a3 3 0 0 1-5-5l2-2" fill="none" stroke="#a0568f" stroke-width="2" stroke-linecap="round"/></svg>
        SolvaneTravelPlanners.com
      </li>
    </ul>
    <div class="brand">
      <span class="brand__dot"></span>
      <span class="brand__name">Solvane Travel Planners</span>
    </div>
    <div class="footer-band"></div>
  </article>
</body>
</html>
```